The attached file is what i need on the front of the card. No details to be changed.

On the back could i have as a heading:
We buy for cash $$$
Deceased estates house lots
Antiques, vintage furniture, bikes, kitchenware, automobile, toys,
sports memorabilia, books, records, signage,farm equipment and fashion.

House

```html
<!DOCTYPE html>
<html lang="en">
<head>
<meta charset="utf-8">
<title>We Buy and Sell – Business Card Front</title>
<link rel="stylesheet" href="https://fonts.googleapis.com/css2?family=Lobster&family=Roboto:wght@700;900&family=Cabin:wght@400;600;700&display=swap">
<style>
  :root {
    --page-bg: #ffffff;
    --band-yellow: #ffff00;
    --card-red: #ff0000;
    --script-red: #e8001a;
    --ink-black: #000000;
    --label-yellow: #ffff00;
    --body-white: #ffffff;
    --card-shadow: rgba(0, 0, 0, 0.55);
  }
  * { margin: 0; padding: 0; box-sizing: border-box; }
  html, body {
    width: 1200px;
    height: 1000px;
    overflow: hidden;
    background: var(--page-bg);
  }
  .card {
    position: absolute;
    left: 95px;
    top: 196px;
    width: 1010px;
    height: 609px;
    background: var(--card-red);
    box-shadow: 0 0 45px 12px var(--card-shadow);
  }
  .card__header {
    height: 188px;
    background: var(--band-yellow);
    text-align: center;
    padding-top: 14px;
  }
  .headline {
    display: flex;
    justify-content: center;
    align-items: center;
    gap: 14px;
    height: 70px;
  }
  .headline__sparkle { width: 30px; height: 38px; margin-top: 4px; }
  .headline__text {
    font-family: "Lobster", cursive;
    font-size: 68px;
    line-height: 1;
    color: var(--script-red);
    letter-spacing: 1px;
    -webkit-text-stroke: 6px #ffffff;
    paint-order: stroke fill;
    text-shadow: 3px 4px 4px rgba(0,0,0,0.7);
    transform: skewX(-6deg);
  }
  .services {
    font-family: "Roboto", Arial, sans-serif;
    font-weight: 700;
    font-size: 25.5px;
    line-height: 31px;
    color: var(--ink-black);
    margin-top: 0;
    padding: 0 20px;
  }
  .card__body {
    position: relative;
    text-align: center;
    font-family: "Cabin", Candara, sans-serif;
    font-size: 25px;
    line-height: 33px;
    color: var(--body-white);
    padding-top: 5px;
  }
  .category__label {
    color: var(--label-yellow);
    font-weight: 700;
  }
  .category--extras { color: var(--label-yellow); font-weight: 700; }
  .stallholder-note {
    position: absolute;
    right: 48px;
    top: 372px;
    font-size: 25px;
  }
</style>
</head>
<body>
  <main class="card">
    <header class="card__header">
      <h1 class="headline">
        <svg class="headline__sparkle" viewBox="0 0 30 38" aria-hidden="true">
          <path d="M15 0 Q17 17 30 19 Q17 21 15 38 Q13 21 0 19 Q13 17 15 0Z" fill="#e8001a"/>
        </svg>
        <span class="headline__text">We buy and sell</span>
        <svg class="headline__sparkle" viewBox="0 0 30 38" aria-hidden="true">
          <path d="M15 0 Q17 17 30 19 Q17 21 15 38 Q13 21 0 19 Q13 17 15 0Z" fill="#e8001a"/>
        </svg>
      </h1>
      <p class="services">Deceased Estates, House Lots, Antiques, Vintage Furniture, Bikes, Kitchenware, Automobile, Toys, Sports Memorabilia, Books, Records, Signage, Farm Equipment and Fashion.</p>
    </header>
    <section class="card__body">
      <p class="category"><span class="category__label">Ceramics:</span> from all eras and from all over the world</p>
      <p class="category"><span class="category__label">Furniture:</span> rustic, restored, chairs, teak, tables</p>
      <p class="category"><span class="category__label">Clothes:</span> mens &amp; ladies, shirts, dresses, shoes, jewellery</p>
      <p class="category"><span class="category__label">Glassware:</span> depression glass, uranium, retro, murano,<br>Scandinavian, Czechoslovakian</p>
      <p class="category"><span class="category__label">Bikes:</span> dragsters, skateboards &amp; bike parts</p>
      <p class="category"><span class="category__label">Kitchenalia:</span> canisters, glasses, utensils items from all eras</p>
      <p class="category">Books: from all eras</p>
      <p class="category"><span class="category__label">Records:</span> a variety of eras 50s, 60s, 70s, 80s</p>
      <p class="category"><span class="category__label">Toys:</span> model cars, pedal cars, dolls</p>
      <p class="category category--extras">Coins &amp; Stamps, Military &amp; Watches and so much more</p>
      <p class="stallholder-note">Stallholder enquiries welcome</p>
    </section>
  </main>
</body>
</html>
```